Wordpress Design Project

I now need a Wordpress theme for my new business.
The business offers consultancy on Information Management, Knowledge Management, Records Management and Document Management.
The winning designer must be able to set up the site for me on my webspace provided by Kestrowave Hosting, or talk me through how to do this.
I already have a logo designed which you can see by viewing my profile on here. I am happy to send copies of the original artwork to bidders.
I recently sold my interest in a very similar business, and want a website similar to (but not the same as) the previous company (who are now my competition!) This website can be viewed at www.trulvanworks.example
Categories will be similar, but I would like everything to be as configurable as possible.
I have a strong preference for clean unfussy design.
I want original design please. Please no templates from free to use sites with stock images... no jigsaw pictures!!!!
Love this one... http://www.quellimar.example/
Please get in touch with any questions.
Reason: All of these are too generic (brief says no jigsaw puzzle images), or have copied TKW which is the COMPETITION - so I don't want the site to look like theirs
Reason: Please keep trying people
Business
Business

```html
<!DOCTYPE html>
<html lang="en">
<head>
<meta charset="utf-8">
<title>Harlowmere Advisory</title>
<link href="https://fonts.googleapis.com/css2?family=Open+Sans:wght@300;400&display=swap" rel="stylesheet">
<style>
:root{
  --ink:#333;
  --body-text:#222;
  --accent:#1e5b94;
  --link:#2a5a8a;
  --footer-text:#f2eee0;
  --rule:#3a3a3a;
  --field:#151515;
  --white:#fff;
}
*{margin:0;padding:0;box-sizing:border-box}
html,body{width:1200px;height:900px;overflow:hidden;background:var(--white);font-family:"Open Sans",Arial,sans-serif;color:var(--ink)}
.page{position:relative;width:1200px;height:900px}

.site-header{position:absolute;left:251px;top:0;width:706px;height:52px}
.brand{position:absolute;left:32px;top:6px;display:flex;align-items:center;gap:7px}
.brand-mark{width:36px;height:36px;border-radius:50%;background:var(--accent)}
.brand-name{font-size:17px;font-weight:400;color:var(--accent);letter-spacing:.6px}
.main-nav{position:absolute;right:71px;top:26px;display:flex;gap:17px;font-size:10.5px;color:#333}

.hero{position:absolute;left:251px;top:52px;width:706px;height:305px;
  background:radial-gradient(ellipse 60% 40% at 50% 0%,#4a4a4a,#1c1c1c 60%,#0e0e0e)}
.hero-slide{position:absolute;left:71px;top:23px;width:564px;height:254px;border:1px solid #8a8a8a;
  background:linear-gradient(180deg,#c9dad6 0%,#dfe9e4 35%,#b9c8a9 65%,#6f7d4f 85%,#4e5a34 100%);
  box-shadow:0 10px 18px rgba(0,0,0,.6)}

.features{position:absolute;left:251px;top:357px;width:706px;height:317px;
  background:linear-gradient(180deg,#efefef 0,#fff 18px,#fff 290px,#ededed 100%)}
.section-title{position:absolute;left:71px;top:21px;font-size:21px;font-weight:300;color:#333}
.feature{position:absolute;width:172px}
.feature-icon{position:absolute;left:0;top:3px;width:26px;height:26px}
.feature-title{position:absolute;left:36px;top:0;font-size:13.5px;font-weight:300;line-height:15px;color:#333;width:150px}
.feature-text{position:absolute;left:0;top:41px;font-size:7.4px;line-height:11.6px;color:var(--body-text);width:168px}
.feature-text .lead{color:var(--link)}

.site-footer{position:absolute;left:251px;top:674px;width:706px;height:226px;
  background:radial-gradient(ellipse 70% 50% at 50% 0%,#2c2c2c,#0d0d0d 70%,#050505)}
.footer-col{position:absolute;top:22px;width:125px}
.footer-title{font-size:13.5px;font-weight:300;color:#eee;margin-bottom:8px;line-height:18px}
.post{display:flex;gap:5px;padding-bottom:6px;margin-bottom:5px;border-bottom:1px solid var(--rule);height:43px}
.post-thumb{width:37px;height:35px;flex:none}
.post-title{font-size:7.3px;line-height:11.5px;color:var(--footer-text)}
.post-date{font-size:7.3px;color:var(--footer-text)}
.meta-list{list-style:none}
.meta-list li{font-size:7.5px;color:var(--footer-text);height:17.3px;padding-top:2px;border-bottom:1px solid var(--rule);display:flex;gap:6px;align-items:flex-start}
.meta-list li::before{content:"";width:3px;height:3px;background:#777;margin-top:4px}
.contact-line{display:flex;gap:7px;font-size:7.5px;color:var(--footer-text);height:14.5px;align-items:flex-start}
.contact-line svg{width:9px;height:9px;flex:none;margin-top:1px}
.contact-line .pad{width:9px}
.keep-title{margin-top:14px}
.social{display:flex;gap:8px}
.social span{width:17px;height:17px;border-radius:3px;background:#4c6f9a}
.form-row{display:flex;align-items:center;gap:6px;margin-bottom:6px;font-size:7.5px;color:var(--footer-text)}
.field{width:82px;height:15px;background:var(--field);border:1px solid var(--rule)}
.message{width:122px;height:58px;background:var(--field);border:1px solid var(--rule);margin-bottom:8px}
.submit{width:48px;height:18px;background:linear-gradient(#fff,#ddd);border-radius:2px;font-size:7.5px;color:#333;display:flex;align-items:center;justify-content:center;font-family:"Courier New",monospace}
</style>
</head>
<body>
<div class="page">
  <header class="site-header">
    <div class="brand"><span class="brand-mark"></span><span class="brand-name">Harlowmere</span></div>
    <nav class="main-nav"><span>Home</span><span>Services</span><span>Approach</span><span>Sectors</span><span>Insights</span><span>Blog</span><span>About</span></nav>
  </header>

  <section class="hero">
    <div class="hero-slide" role="img" aria-label="Photograph of a pink cosmos flower against a cloudy sky with a blurred meadow"></div>
  </section>

  <section class="features">
    <h2 class="section-title">Why Choose Us</h2>

    <div class="feature" style="left:71px;top:61px">
      <svg class="feature-icon" viewBox="0 0 26 26"><defs><linearGradient id="wheel" x1="0" y1="0" x2="1" y2="1"><stop offset="0" stop-color="#f33"/><stop offset=".35" stop-color="#fd3"/><stop offset=".65" stop-color="#3c6"/><stop offset="1" stop-color="#36f"/></linearGradient></defs><circle cx="13" cy="13" r="12" fill="url(#wheel)"/></svg>
      <div class="feature-title">Information Management Strategy</div>
      <p class="feature-text">We map the information you hold, <span class="lead">who owns it</span> and how it moves, then shape a clear plan that fits your goals and budget.</p>
    </div>
    <div class="feature" style="left:267px;top:61px">
      <svg class="feature-icon" viewBox="0 0 26 26"><rect x="3" y="3" width="20" height="15" fill="#eee" stroke="#999"/><rect x="6" y="7" width="14" height="8" fill="#d88"/><path d="M8 18l-3 7M18 18l3 7" stroke="#a86" stroke-width="1.5"/></svg>
      <div class="feature-title">Knowledge Management Consulting</div>
      <p class="feature-text">Capture what your people know before it walks out of the door. <span class="lead">We build simple habits</span> and tools that keep expertise shared.</p>
    </div>
    <div class="feature" style="left:463px;top:61px">
      <svg class="feature-icon" viewBox="0 0 26 26"><path d="M4 24L18 8" stroke="#555" stroke-width="3"/><circle cx="20" cy="6" r="3" fill="#f7c23a"/></svg>
      <div class="feature-title">Records Management Programmes</div>
      <p class="feature-text">Retention schedules, file plans and audit trails that stand up to scrutiny. <span class="lead">Stay compliant</span> without drowning in paper.</p>
    </div>

    <div class="feature" style="left:71px;top:178px">
      <svg class="feature-icon" viewBox="0 0 26 26"><rect x="2" y="3" width="22" height="20" rx="3" fill="#d8d8d8" stroke="#888"/><rect x="9" y="7" width="8" height="12" fill="#fff" stroke="#555"/></svg>
      <div class="feature-title">Document Management Systems</div>
      <p class="feature-text">Independent advice on choosing, configuring and rolling out the <span class="lead">right system</span>, so documents are easy to store and find.</p>
    </div>
    <div class="feature" style="left:267px;top:178px">
      <svg class="feature-icon" viewBox="0 0 26 26"><path d="M6 20a5 5 0 0 1 1-10 7 7 0 0 1 13 2 4 4 0 0 1 0 8z" fill="#e8eef2" stroke="#9ab"/><circle cx="19" cy="19" r="4" fill="#5a5"/></svg>
      <div class="feature-title">Governance And Data Protection</div>
      <p class="feature-text">Practical policies for privacy, security and information risk, written in <span class="lead">plain language</span> your whole team can follow.</p>
    </div>
    <div class="feature" style="left:463px;top:178px">
      <svg class="feature-icon" viewBox="0 0 26 26"><circle cx="13" cy="14" r="9" fill="#4bb3d6"/></svg>
      <div class="feature-title">Training And Ongoing Support</div>
      <p class="feature-text">Workshops and coaching that help staff adopt new ways of working, with <span class="lead">friendly support</span> long after launch day.</p>
    </div>
  </section>

  <footer class="site-footer">
    <div class="footer-col" style="left:71px">
      <h3 class="footer-title">Popular Posts</h3>
      <div class="post"><div class="post-thumb" role="img" aria-label="Thumbnail of pale blossoms against the sky" style="background:linear-gradient(#bcd0df,#d9c6cf)"></div><div><div class="post-title">Retention schedules made simple</div><div class="post-date">Sep 30, 2010</div></div></div>
      <div class="post"><div class="post-thumb" role="img" aria-label="Thumbnail of white cherry blossoms" style="background:linear-gradient(#8fb0d6,#e6e0ea)"></div><div><div class="post-title">Why records matter</div><div class="post-date">Sep 27, 2010</div></div></div>
      <div class="post"><div class="post-thumb" role="img" aria-label="Thumbnail of a white flower in green grass" style="background:linear-gradient(#3f7a2a,#6aa040)"></div><div><div class="post-title">Choosing a DMS</div><div class="post-date">Sep 30, 2010</div></div></div>
    </div>

    <div class="footer-col" style="left:218px">
      <h3 class="footer-title">Meta</h3>
      <ul class="meta-list"><li>Site Admin</li><li>Log out</li><li>Entries RSS</li><li>Comments RSS</li><li>Platform.example</li></ul>
    </div>

    <div class="footer-col" style="left:364px">
      <h3 class="footer-title">Contact Us</h3>
      <div class="contact-line"><svg viewBox="0 0 10 10"><path d="M2 1l2 2-1 1.5c.8 1.5 1.5 2.2 3 3L7.5 6 9.5 8 8 9.5C4.5 9 1 5.5.5 2z" fill="#aaa"/></svg>(+00) 555 010 200</div>
      <div class="contact-line"><svg viewBox="0 0 10 10"><rect x=".5" y="2" width="9" height="6" fill="none" stroke="#aaa"/><path d="M.5 2L5 5.5 9.5 2" fill="none" stroke="#aaa"/></svg>hello@harlowmere.example</div>
      <div class="contact-line"><svg viewBox="0 0 10 10"><path d="M5 .5L.5 5H2v4h2.5V6.5h1V9H8V5h1.5z" fill="#aaa"/></svg>the address</div>
      <div class="contact-line"><span class="pad"></span>city, state &nbsp;1111</div>
      <h3 class="footer-title keep-title">Keep In Touch</h3>
      <div class="social"><span></span><span style="background:#8a8a95"></span><span style="background:#3d79a8"></span><span style="background:#5a7fa8"></span><span style="background:#5fa8c8"></span></div>
    </div>

    <div class="footer-col" style="left:511px">
      <h3 class="footer-title">Email Us</h3>
      <div class="form-row"><span class="field"></span>Name *</div>
      <div class="form-row"><span class="field"></span>Email *</div>
      <div class="message"></div>
      <div class="submit">Submit</div>
    </div>
  </footer>
</div>
</body>
</html>
```